Food company needs to improve packaging design

Objective:
We are looking for a graphic designer to help improve and elevate the design of our tortilla chips packaging. We’ve created a draft version that we will provide as a reference, but we’re open to creative input and fresh ideas to make the design more appealing and shelf-ready.

Scope of Work:

Redesign the front of the packaging, with room for creative freedom.

You may change the background, colors, and overall layout if you believe it enhances the design.

The back of the packaging should remain unchanged, but you are welcome to propose minor visual tweaks if necessary for consistency.

Design Goals:

Create a bold, appealing design that stands out on shelves.

Maintain clarity and readability of all key product information.

Reflect a fresh, natural, and high-quality product image.

Deliverables:

Print-ready files (preferably AI or PSD with layers).

High-resolution mockups.

Any font files or external assets used.

Additional Notes:

We’re open to different design directions, so feel free to explore concepts.

We will need to finish writing the copy for the back, but we have already created some space for it. Please do not remove the space.

We have attached the branding guide, but we have freedom on the font for the packaging. We have also attached a different packaging to show that we don't necessarily have to use the colors from our branding guide for the background. However, if you decide to go away from our colors, please choose them carefully and provide another design option with our green as the background to compare.

You will also find the blank die line cut to work on your design.

Please ensure that the design remains practical for commercial printing and meets basic packaging guidelines.

```html
<!DOCTYPE html>
<html lang="en">
<head>
<meta charset="utf-8">
<title>Kelva Tortilla Chips – Sea Salt</title>
<link rel="stylesheet" href="https://fonts.googleapis.com/css2?family=Lilita+One&family=Oswald:wght@500;600&family=Montserrat:wght@500;600;700&family=Great+Vibes&display=swap">
<style>
  :root {
    --backdrop: #eeeeee;
    --bag-green: #7fcb4a;
    --bag-green-light: #9ad866;
    --bag-blue: #3c5f8a;
    --bag-blue-dark: #2f4d74;
    --panel-white: #fbfbfa;
    --ink-dark: #3b3735;
    --ink-shadow: #c9b79c;
    --leaf-green: #3f8a2c;
    --caramel: #b4792a;
    --ribbon-red: #7e2630;
    --pill-green: #5fae3a;
    --pill-red: #d8262b;
    --chip-gold: #e9b43c;
    --salsa: #b83a22;
  }
  * { box-sizing: border-box; margin: 0; padding: 0; }
  html, body { width: 1200px; height: 1013px; overflow: hidden; }
  body { background: var(--backdrop); font-family: "Montserrat", sans-serif; position: relative; }

  .bag { position: absolute; left: 325px; top: 123px; width: 490px; height: 784px; }
  .bag-shape { position: absolute; inset: 0; }
  .bag > * { position: absolute; }

  .brand { left: 0; width: 100%; top: 78px; text-align: center; color: #fff; }
  .brand-name { font-family: "Montserrat", sans-serif; font-weight: 700; font-size: 46px; letter-spacing: 2px; line-height: 1; }
  .brand-sub { font-family: "Montserrat", sans-serif; font-weight: 600; font-size: 13px; letter-spacing: 3px; margin-top: 6px; }

  .ribbon { left: 368px; top: 42px; width: 66px; height: 119px; }
  .ribbon-text { left: 368px; top: 78px; width: 66px; text-align: center; color: #fff; }
  .ribbon-icon { display: block; margin: 0 auto 4px; }
  .ribbon-pct { font-family: "Oswald", sans-serif; font-weight: 600; font-size: 21px; line-height: 1; }
  .ribbon-note { font-size: 7px; font-weight: 600; margin-top: 4px; }

  .title-panel { left: 81px; top: 164px; width: 337px; height: 233px; }
  .title-text { left: 81px; top: 178px; width: 337px; text-align: center; }
  .kicker { display: flex; align-items: center; justify-content: center; gap: 10px; font-family: "Oswald", sans-serif; font-weight: 600; font-size: 21px; color: var(--leaf-green); }
  .kicker::before, .kicker::after { content: ""; width: 34px; height: 3px; background: var(--leaf-green); }
  .product-name { font-family: "Lilita One", sans-serif; font-size: 62px; line-height: 64px; color: var(--ink-dark); text-shadow: 3px 3px 0 var(--ink-shadow); margin-top: 6px; letter-spacing: 1px; }
  .claims { font-family: "Oswald", sans-serif; font-weight: 600; font-size: 19px; color: var(--caramel); margin-top: 6px; }

  .serving-photo { left: 70px; top: 405px; width: 370px; height: 300px; border-radius: 46% 46% 40% 40%; background: radial-gradient(ellipse at 55% 45%, var(--chip-gold) 0%, #dca23a 38%, var(--salsa) 62%, #f4f1ec 78%, rgba(244,241,236,0) 80%); }

  .seal { left: 352px; top: 440px; width: 80px; height: 80px; }

  .flavour { left: 289px; top: 596px; width: 157px; height: 62px; background: #fff; border-radius: 12px 0 0 12px; display: flex; align-items: center; justify-content: center; font-family: "Great Vibes", cursive; font-size: 38px; color: #222; }

  .nutrition { left: 82px; top: 595px; display: grid; grid-template-columns: repeat(3, 31px); column-gap: 4px; row-gap: 8px; }
  .pill { width: 31px; height: 66px; background: #fff; border-radius: 16px; display: flex; flex-direction: column; align-items: center; padding-top: 3px; }
  .pill-mark { width: 25px; height: 25px; border-radius: 50%; display: flex; align-items: center; justify-content: center; color: #fff; font-weight: 700; text-align: center; }
  .pill-mark.ours { background: var(--pill-green); font-size: 6px; letter-spacing: .2px; }
  .pill-mark.theirs { background: var(--pill-red); font-size: 4.5px; line-height: 1.1; }
  .pill-label { font-size: 3.5px; color: #555; margin-top: 6px; font-weight: 600; }
  .pill-value { font-size: 10px; font-weight: 700; color: #222; margin-top: 2px; }
  .pill-value small { font-size: 5px; }

  .net-weight { left: 375px; top: 722px; font-size: 12px; font-weight: 600; color: #fff; }
</style>
</head>
<body>
<main class="bag" aria-label="Tortilla chips bag front">
  <svg class="bag-shape" width="490" height="784" viewBox="0 0 490 784">
    <defs>
      <linearGradient id="greenFill" x1="0" y1="0" x2="1" y2="0">
        <stop offset="0" stop-color="var(--bag-green)"/>
        <stop offset=".5" stop-color="var(--bag-green-light)"/>
        <stop offset="1" stop-color="var(--bag-green)"/>
      </linearGradient>
    </defs>
    <path d="M0 6 L490 0 L488 784 L4 784 Z" fill="url(#greenFill)"/>
    <rect x="0" y="0" width="490" height="22" fill="var(--bag-green)"/>
    <path d="M2 520 Q245 470 488 500 L488 760 L4 760 Z" fill="var(--bag-blue)"/>
    <path d="M4 740 L488 740 L488 760 L4 760 Z" fill="var(--bag-blue-dark)"/>
    <rect x="0" y="760" width="490" height="24" fill="var(--bag-green)"/>
  </svg>

  <header class="brand">
    <div class="brand-name">KELVA</div>
    <div class="brand-sub">SNACKWORKS</div>
  </header>

  <svg class="ribbon" viewBox="0 0 66 119" aria-hidden="true">
    <path d="M0 0 H66 V104 L33 119 L0 104 Z" fill="var(--ribbon-red)"/>
    <path d="M6 4 V101 L33 113 L60 101 V4" fill="none" stroke="#fff" stroke-width="1" stroke-dasharray="4 3"/>
  </svg>
  <div class="ribbon-text">
    <svg class="ribbon-icon" width="18" height="20" viewBox="0 0 18 20" aria-hidden="true">
      <path d="M8 1 C12 6 15 9 14 14 A6 6 0 0 1 2 14 C2 10 5 8 8 1 Z" fill="#fff"/>
      <circle cx="13" cy="14" r="4" fill="var(--ribbon-red)" stroke="#fff" stroke-width="1.2"/>
      <path d="M13 12 V16 M11.5 14.5 L13 16 L14.5 14.5" stroke="#fff" stroke-width="1.1" fill="none"/>
    </svg>
    <div class="ribbon-pct">81%</div>
    <div class="ribbon-note">Less Calories</div>
  </div>

  <svg class="title-panel" viewBox="0 0 337 233" aria-hidden="true">
    <path d="M4 6 L40 2 L80 7 L130 1 L180 6 L230 2 L280 6 L333 3 L330 40 L336 90 L331 140 L336 190 L332 230 L280 226 L230 231 L180 226 L130 231 L80 226 L30 231 L3 228 L7 180 L1 130 L6 80 L1 40 Z" fill="var(--panel-white)"/>
  </svg>
  <section class="title-text">
    <p class="kicker">FRESHLY MADE</p>
    <h1 class="product-name">TORTLLA<br>CHIPS</h1>
    <p class="claims">KETO · LOW CARB · FAT FREE</p>
  </section>

  <div class="serving-photo" role="img" aria-label="Photo of tortilla chips resting in a bowl of red salsa with a red chili pepper and parsley"></div>

  <svg class="seal" viewBox="0 0 80 80" aria-label="Inhibits absorption of carbs and fats – all-natural inhibitors">
    <circle cx="40" cy="40" r="39" fill="#fff"/>
    <circle cx="40" cy="40" r="35" fill="var(--ribbon-red)"/>
    <circle cx="40" cy="40" r="22" fill="none" stroke="#fff" stroke-width=".8"/>
    <path id="sealArc" d="M12 40 A28 28 0 0 1 68 40" fill="none"/>
    <path id="sealArcLow" d="M14 44 A26 26 0 0 0 66 44" fill="none"/>
    <text font-size="6.5" font-weight="700" fill="#fff" font-family="Montserrat, sans-serif"><textPath href="#sealArc" startOffset="50%" text-anchor="middle">Inhibits Absorption</textPath></text>
    <text font-size="6.5" font-weight="700" fill="#fff" font-family="Montserrat, sans-serif"><textPath href="#sealArcLow" startOffset="50%" text-anchor="middle">of Carbs and Fats</textPath></text>
    <path d="M40 26 C46 28 46 34 40 36 C34 34 34 28 40 26 Z" fill="#fff"/>
    <text x="40" y="44" font-size="5.5" font-weight="700" fill="#fff" text-anchor="middle" font-family="Montserrat, sans-serif">All-Natural</text>
    <text x="40" y="51" font-size="5.5" font-weight="700" fill="#fff" text-anchor="middle" font-family="Montserrat, sans-serif">Inhibitors</text>
  </svg>

  <div class="flavour">Sea Salt</div>

  <section class="nutrition" aria-label="Nutrition comparison">
    <div class="pill"><span class="pill-mark ours">KELVA</span><span class="pill-label">CALORIES</span><span class="pill-value">28</span></div>
    <div class="pill"><span class="pill-mark ours">KELVA</span><span class="pill-label">CARBS</span><span class="pill-value">2<small>g</small></span></div>
    <div class="pill"><span class="pill-mark ours">KELVA</span><span class="pill-label">FATS</span><span class="pill-value">0<small>g</small></span></div>
    <div class="pill"><span class="pill-mark theirs">LEADING<br>BRAND</span><span class="pill-label">CALORIES</span><span class="pill-value">150</span></div>
    <div class="pill"><span class="pill-mark theirs">LEADING<br>BRAND</span><span class="pill-label">CARBS</span><span class="pill-value">15<small>g</small></span></div>
    <div class="pill"><span class="pill-mark theirs">LEADING<br>BRAND</span><span class="pill-label">FATS</span><span class="pill-value">9<small>g</small></span></div>
  </section>

  <p class="net-weight">Net Wt. 8 oz (224g)</p>
</main>
</body>
</html>
```